International Property Consultancy

Brief Overview:

I need a dynamic and well designed website that is easy to use and understand. It has to be unique and different to generic templates that most websites seem to be these days. PLEASE NO GENERIC TEMPLATES FROM THE INTERNET.

Our business has 10 years experience working on struggling international developments that we then work in-house for to turn around and brings bout success. We stay within a project often for long periods of time until success is achieved. We are unique in our approach and completely different to the standard routes to market for many developments. The site is for developers to see what we have done in regards to previous projects, as such we want to incorporate video into this site with a strong design aesthetic. There will be videos of the past projects we have worked on, which will act as case studies.

I like very simple but punchy websites, that people can navigate and understand very easily. Also a big fan of unique and well thought out design aesthetic.

Initial Site layout thoughts:

1) Homepage:
2) About Us
3) What we've done / Work
This part has the projects we have worked on (France, Portugal, London, Morocco). Each one will have some video content and photo images, but also would be good to have a succinct way to mention what we did and the successes in a clever and punchy way.

4) Contact Us

* This is just a guideline. Would be open to input and creative direction on your own part.

*More details and websites we like can be seen in the brief doc attached.

PLEASE VIEW THE WIREFRAME WORD DOC ATTACHED.

Here there are also some more examples to help:

Here are just a few examples of websites and what I like about them:

- www.velmoro.com (clean, nice geometric design aesthetic, good animation when loading and changing pages well thought out all though also coulee be considered a bit dull and basic after the initial homepage slide)
- https://www.farbridgehub.net (Clean site, quite clinical, lacks video content and doesn't engage greatly).
- https://ruskotile.com (minimal, and like how it mixes the design aesthetic more with video and photo content)

- https://www.amberquillworks.com (like the layout of this and how it displays the projects and work section)

- https://brisk.com (Good use of video content)

- https://loomfield.studio (minimal to the point and mixes design with video and animation etc...)

Here is another couple of cool websites that may help give you some direction: https://halvenquay.com www.brisk.com

Hi there, One of the things I thought would be good on the homepage is to add the logo with a 'digital landscape' before flicking down into a slide with video content of the projects... Just an idea but have posted some pics in the brief. We would get this animated for the site. But if you have better ideas, please do run with them. Thanks,

Target Market(s)

Property developers

Number of Pages Required

4 page

Font styles to use
Other font styles liked:
• Read brief

Requirements
Must have
• Needs to be clean, dynamic and easy to follow on desktop and mobile. We will use it as a kind of portfolio website so will need to embed video of past projects we have worked on.

Read brief in docs.
Nice to have
• Clean
Should not have
• Not be another generic template website.
Not have random property stock photos. (We are not a property agency).

```html
<!DOCTYPE html>
<html lang="en">
<head>
<meta charset="utf-8">
<title>Orvandel — Work</title>
<link href="https://fonts.googleapis.com/css2?family=Poppins:wght@400;500;600;700;800&display=swap" rel="stylesheet">
<style>
:root{
  --navy:#23304f;
  --ink:#233052;
  --body:#4a5064;
  --white:#ffffff;
  --mist:#f4f5f8;
  --rule:#dfe2e8;
  --icon:#a9aebb;
  --plum:#5a3a52;
  --sky:#5a8de6;
  --terra:#e2683f;
}
*{box-sizing:border-box;margin:0;padding:0}
html,body{width:978px;height:1200px;overflow:hidden}
body{position:relative;background:var(--white);font-family:'Poppins',sans-serif;color:var(--ink)}
.abs{position:absolute}

.brand{left:72px;top:30px;font-size:33px;font-weight:500;letter-spacing:-.5px;color:var(--ink)}
.nav{top:42px;font-size:11px;font-weight:600;letter-spacing:.3px;color:var(--ink)}
.nav-active{left:750px;top:0;width:46px;height:3px;background:var(--navy)}

.page-title{left:72px;top:168px;font-size:55px;font-weight:800;letter-spacing:-.5px;color:var(--ink)}
.page-intro{left:72px;top:238px;width:490px;font-size:12.4px;line-height:18px;color:var(--body)}
.see-work{left:782px;top:219px;font-size:14px;font-weight:700;letter-spacing:.3px;color:var(--ink);padding-bottom:1px;border-bottom:1.5px solid var(--ink);width:123px}

.projects{left:0;top:322px;width:978px;height:426px;background:var(--navy);overflow:hidden}
.card{top:80px;width:212px;height:275px;box-shadow:0 26px 22px -16px rgba(10,16,32,.55)}
.card-france{left:148px;background:linear-gradient(180deg,#fdecd3 0%,#fdecd3 45%,#e9b596 75%,#7a4f68 100%)}
.card-portugal{left:458px;background:linear-gradient(180deg,#cfe7ef 0%,#cfe7ef 50%,#9fd6d8 75%,#6f8fe0 100%)}
.card-morocco{left:776px;width:202px;background:linear-gradient(180deg,#f8e6ea 0%,#f8e6ea 25%,#f2cf9a 45%,#e2683f 70%,#d85d36 100%)}
.country{top:100px;font-size:42px;font-weight:700;line-height:1;color:var(--white);letter-spacing:-.2px}
.c-france{left:79px}
.c-portugal{left:392px}
.c-morocco{left:697px}
.plum{color:var(--plum)}
.sky{color:var(--sky)}
.terra{color:var(--terra)}

.contact{left:0;top:748px;width:978px;height:452px;background:var(--mist)}
.contact-title{left:106px;top:804px;font-size:42px;font-weight:700;color:var(--ink);letter-spacing:.2px}
.office{top:880px;width:240px}
.office h3{font-size:18px;font-weight:600;color:var(--ink);margin-bottom:16px}
.detail{position:relative;padding-left:19px;margin-bottom:13px}
.detail svg{position:absolute;left:0;top:3px;width:11px;height:11px}
.detail .label{font-size:11.5px;font-weight:600;color:var(--ink);line-height:17px}
.detail .value{font-size:11.5px;color:var(--body);line-height:18px}

.footer-rule{left:71px;top:1139px;width:833px;height:1px;background:var(--rule)}
.footer-text{top:1160px;font-size:11.5px;font-weight:500;color:var(--ink)}
.social{top:1155px;width:28px;height:28px;border-radius:50%;background:var(--navy)}
</style>
</head>
<body>
  <div class="abs brand">orvandel.</div>
  <div class="abs nav-active"></div>
  <div class="abs nav" style="left:585px">HOME</div>
  <div class="abs nav" style="left:658px">ABOUT US</div>
  <div class="abs nav" style="left:755px">WORK</div>
  <div class="abs nav" style="left:829px">CONTACT US</div>

  <h1 class="abs page-title">Work</h1>
  <p class="abs page-intro">We deliver a unique and truly bespoke approach to delivering international developments to market, with over 10 years success around the world.</p>
  <div class="abs see-work">SEE OUR ‘WORK’</div>

  <section class="abs projects">
    <div class="abs card card-france" role="img" aria-label="Illustrated Paris skyline with the Eiffel Tower, a glass pyramid and domed buildings"></div>
    <div class="abs card card-portugal" role="img" aria-label="Illustrated Lisbon skyline with a suspension bridge and modern towers"></div>
    <div class="abs card card-morocco" role="img" aria-label="Illustrated Moroccan kasbah with palm trees under a warm sun"></div>
    <div class="abs country c-france">Fra<span class="plum">nce</span></div>
    <div class="abs country c-portugal">Por<span class="sky">tugal</span></div>
    <div class="abs country c-morocco">Mor<span class="terra">oco</span></div>
  </section>

  <section class="abs contact"></section>
  <h2 class="abs contact-title">Contact Us</h2>

  <div class="abs office" style="left:106px">
    <h3>France</h3>
    <div class="detail"><svg viewBox="0 0 12 12"><rect x="0" y="2" width="12" height="8" fill="var(--icon)"/><path d="M0 2 L6 7 L12 2" fill="none" stroke="var(--mist)" stroke-width="1"/></svg><div class="label">Email:</div><div class="value">www.example.com</div></div>
    <div class="detail"><svg viewBox="0 0 12 12"><path d="M2 1 L4 1 L5 4 L3.5 5 Q5 8 7 8.5 L8 7 L11 8 L11 10 Q10 11.5 8 11 Q2 9 1 3 Q1 1.5 2 1Z" fill="var(--icon)"/></svg><div class="label">Phone:</div><div class="value">1 (+08) 123-456-78</div></div>
    <div class="detail"><svg viewBox="0 0 12 12"><path d="M6 0.5 A4 4 0 0 1 10 4.5 C10 7.5 6 11.5 6 11.5 C6 11.5 2 7.5 2 4.5 A4 4 0 0 1 6 0.5Z" fill="var(--icon)"/><circle cx="6" cy="4.5" r="1.5" fill="var(--mist)"/></svg><div class="label">Location:</div><div class="value">Some address line goes<br>here city name</div></div>
  </div>

  <div class="abs office" style="left:411px">
    <h3>Portugal</h3>
    <div class="detail"><svg viewBox="0 0 12 12"><rect x="0" y="2" width="12" height="8" fill="var(--icon)"/><path d="M0 2 L6 7 L12 2" fill="none" stroke="var(--mist)" stroke-width="1"/></svg><div class="label">Email:</div><div class="value">www.example.com</div></div>
    <div class="detail"><svg viewBox="0 0 12 12"><path d="M2 1 L4 1 L5 4 L3.5 5 Q5 8 7 8.5 L8 7 L11 8 L11 10 Q10 11.5 8 11 Q2 9 1 3 Q1 1.5 2 1Z" fill="var(--icon)"/></svg><div class="label">Phone:</div><div class="value">1 (+08) 123-456-78</div></div>
    <div class="detail"><svg viewBox="0 0 12 12"><path d="M6 0.5 A4 4 0 0 1 10 4.5 C10 7.5 6 11.5 6 11.5 C6 11.5 2 7.5 2 4.5 A4 4 0 0 1 6 0.5Z" fill="var(--icon)"/><circle cx="6" cy="4.5" r="1.5" fill="var(--mist)"/></svg><div class="label">Location:</div><div class="value">Some address line goes<br>here city name</div></div>
  </div>

  <div class="abs office" style="left:715px">
    <h3>London</h3>
    <div class="detail"><svg viewBox="0 0 12 12"><rect x="0" y="2" width="12" height="8" fill="var(--icon)"/><path d="M0 2 L6 7 L12 2" fill="none" stroke="var(--mist)" stroke-width="1"/></svg><div class="label">Email:</div><div class="value">www.example.com</div></div>
    <div class="detail"><svg viewBox="0 0 12 12"><path d="M2 1 L4 1 L5 4 L3.5 5 Q5 8 7 8.5 L8 7 L11 8 L11 10 Q10 11.5 8 11 Q2 9 1 3 Q1 1.5 2 1Z" fill="var(--icon)"/></svg><div class="label">Phone:</div><div class="value">1 (+08) 123-456-78</div></div>
    <div class="detail"><svg viewBox="0 0 12 12"><path d="M6 0.5 A4 4 0 0 1 10 4.5 C10 7.5 6 11.5 6 11.5 C6 11.5 2 7.5 2 4.5 A4 4 0 0 1 6 0.5Z" fill="var(--icon)"/><circle cx="6" cy="4.5" r="1.5" fill="var(--mist)"/></svg><div class="label">Location:</div><div class="value">Some address line goes<br>here city name</div></div>
  </div>

  <div class="abs footer-rule"></div>
  <div class="abs footer-text" style="left:105px">© 2020 Orvandel. All Rights Reserved</div>
  <div class="abs footer-text" style="left:386px">Privacy</div>
  <div class="abs footer-text" style="left:451px">Terms of use</div>
  <div class="abs social" style="left:770px" role="img" aria-label="Social profile link"></div>
  <div class="abs social" style="left:807px" role="img" aria-label="Social profile link"></div>
  <div class="abs social" style="left:841px" role="img" aria-label="Social profile link"></div>
</body>
</html>
```